Bright Kestrel Studio - Redesign of our website - needs to be dynamic and alive!

We provide fun lessons exclusively in students' homes in music, art, yoga and acting. I like most of the graphics and copy on the site now, but it looks too static and there might be too much info to read on the home page. Needs movement, needs to generate excitement and be a fun place to visit, yet keeping professional-looking. The site needs better SEO, a better look and needs to generate more business, as several people see it each day but few contact us for details about our program. The site is brightkestrel-studio.test. I'd like it to continue to be hosted on my domain in Wordpress format so I can add and delete teacher photos from time to time. I like the way the teachers' bios currently pop up when a cursor is hovered over them on the Our Team page. Thank you and good luck!

Target Market(s)

Wealthy, college-educated households with children who live in the Greater Atlanta area

Industry/Entity Type

Education

Coding

Number of Pages Required

Requirements
Must have
• Home Page movement, excitement, but keeping it professional-looking. We're an educational company and want to market to people who are looking for a professional yet fun/exciting approach to lessons in their homes.
Nice to have
• The info on the Testimonials page can probably rotate and fade in/fade out on the home page or slide on/slide off instead of having a separate page for these.
• The info on the Trial Lessons page can probably be included as a banner on the home page too instead of being a separate page. Nice if I can change the text on this myself from time to time to mention any promotions I might be offering with regard to trial lessons.

```html
<!DOCTYPE html>
<html lang="en">
<head>
<meta charset="utf-8">
<title>Bright Kestrel Studio – In-Home Lessons</title>
<link href="https://fonts.googleapis.com/css2?family=Open+Sans:wght@400;600;700&family=Roboto+Condensed:wght@400;700&display=swap" rel="stylesheet">
<style>
:root{
  --purple:#5b2c83;
  --teal:#1aa3cc;
  --teal-dark:#0f86aa;
  --orange:#ea6330;
  --yellow:#f6b40f;
  --sky:#1ea4d6;
  --lime:#8bc43f;
  --tangerine:#ee6a31;
  --ink:#2b2b2b;
  --body:#555;
  --muted:#8a8a8a;
  --line:#dcdcdc;
  --grey-bg:#f1f2f4;
  --white:#fff;
  --star:#f5b400;
}
*{margin:0;padding:0;box-sizing:border-box}
html,body{width:1200px;height:3364px;overflow:hidden}
body{position:relative;background:var(--white);font-family:"Open Sans",Arial,sans-serif;color:var(--body);font-size:12px;line-height:1.6}
.abs{position:absolute}
.cond{font-family:"Roboto Condensed","Arial Narrow",sans-serif}

/* header */
.brand{left:99px;top:30px;display:flex;align-items:center;gap:12px}
.brand-dot{width:46px;height:46px;border-radius:50%;background:var(--purple)}
.brand-name{font-family:"Roboto Condensed",sans-serif;font-weight:700;font-size:30px;line-height:1;color:var(--purple);width:190px}
.head-phone{left:768px;top:56px;display:flex;align-items:center;gap:8px;font-family:"Roboto Condensed",sans-serif;font-size:22px;color:var(--purple)}
.social{left:985px;top:56px;display:flex;gap:6px}
.social span{width:24px;height:24px;border-radius:50%;border:1.5px solid var(--teal)}
.social span:last-child{border-color:#d9453a}

.nav{left:0;top:139px;width:1200px;height:49px;background:var(--teal)}
.nav ul{list-style:none;display:flex;position:absolute;left:99px;top:0;height:49px}
.nav li{font-family:"Roboto Condensed",sans-serif;font-size:13px;color:var(--white);text-transform:uppercase;height:49px;line-height:49px;padding:0 22px}
.nav li.active{background:var(--teal-dark)}

/* hero */
.hero{left:0;top:188px;width:1200px;height:487px;background:linear-gradient(100deg,#3a3530 0%,#6b5e52 40%,#8e8478 62%,#4a443e 100%)}
.hero-title{left:96px;top:355px;font-family:"Roboto Condensed",sans-serif;font-size:50px;color:var(--white);line-height:1}
.hero-sub{left:96px;top:412px;width:330px;color:var(--white);font-size:15px;line-height:1.3}
.hero-btn{left:96px;top:469px;width:144px;height:36px;background:var(--orange);color:var(--white);font-family:"Roboto Condensed",sans-serif;font-size:14px;display:flex;align-items:center;justify-content:center;gap:6px;border-radius:3px}
.hero-arrow{top:418px;width:32px;height:32px;border-radius:50%;background:rgba(0,0,0,.45);display:flex;align-items:center;justify-content:center}

/* section headings */
.sec-title{left:0;width:1200px;text-align:center;font-family:"Roboto Condensed",sans-serif;font-size:32px;color:var(--ink)}

/* courses */
.course{top:790px;width:233px;height:349px;border-radius:8px;overflow:hidden;box-shadow:0 6px 10px rgba(0,0,0,.12)}
.course-photo{height:164px}
.course-body{height:185px;text-align:center;color:var(--white);position:relative;padding-top:32px}
.course-icon{position:absolute;left:92px;top:-26px;width:50px;height:50px;border-radius:50%;border:2px solid rgba(255,255,255,.85);display:flex;align-items:center;justify-content:center}
.course h3{font-family:"Roboto Condensed",sans-serif;font-size:20px;font-weight:400;margin-top:10px}
.course p{font-size:10.5px;font-weight:600;line-height:1.45;padding:2px 22px 0}
.course-btn{display:inline-block;margin-top:14px;width:96px;height:28px;line-height:25px;border:1.5px solid var(--white);border-radius:14px;font-size:10px}
.c-yellow .course-body,.c-yellow .course-icon{background:var(--yellow)}
.c-blue .course-body,.c-blue .course-icon{background:var(--sky)}
.c-green .course-body,.c-green .course-icon{background:var(--lime)}
.c-orange .course-body,.c-orange .course-icon{background:var(--tangerine)}

/* welcome */
.welcome-photo{left:101px;top:1200px;width:314px;height:336px;background:radial-gradient(ellipse at 50% 55%,#e7c6ad 0%,#a57a62 30%,#f4f1ef 62%,#fff 75%)}
.welcome{left:480px;top:1250px;width:620px}
.welcome h2{font-family:"Roboto Condensed",sans-serif;font-weight:400;font-size:33px;color:var(--ink);line-height:1}
.welcome h4{font-size:14px;font-weight:600;color:#444;margin:18px 0 8px}
.welcome p{font-size:11.5px;line-height:1.85;margin-bottom:8px}
.btn-outline{display:inline-flex;align-items:center;gap:6px;margin-top:22px;height:36px;padding:0 14px;border:1.5px solid #999;color:#444;font-size:11px;font-weight:600}

/* programs */
.programs-bg{left:0;top:1560px;width:1200px;height:620px}
.programs-photo{left:830px;top:1637px;width:370px;height:489px;background:linear-gradient(160deg,#f4efe9 0%,#d9b598 28%,#3b3b40 55%,#e9e9ea 100%)}
.programs{left:99px;top:1683px;width:560px}
.programs h2{font-family:"Roboto Condensed",sans-serif;font-weight:400;font-size:33px;color:var(--ink);line-height:1}
.programs .intro{font-size:11.5px;line-height:1.85;margin-top:16px}
.prog{position:absolute;left:0;width:560px}
.prog-icon{position:absolute;left:0;top:0;width:62px;height:62px;border-radius:50%;border:1.5px solid #777;display:flex;align-items:center;justify-content:center;background:var(--white)}
.prog h4{margin-left:78px;font-family:"Roboto Condensed",sans-serif;font-size:16px;color:#333;font-weight:400}
.prog p{margin-left:78px;font-size:11px;line-height:1.8;margin-top:4px}
.prog-line{position:absolute;left:31px;width:1.5px;background:#888}

/* blog */
.post{top:2281px;width:310px;text-align:center}
.post-photo{height:183px;background:linear-gradient(135deg,#3e3128 0%,#8a6c54 45%,#2d2521 100%)}
.post h3{background:var(--white);margin:-20px 16px 0;position:relative;padding-top:10px;font-size:16px;font-weight:400;color:#333}
.post .meta{font-size:11px;font-style:italic;color:var(--teal);margin-top:8px}
.post .meta b{color:#999;font-weight:400;margin:0 10px}
.post p{font-size:11px;line-height:1.55;margin-top:4px;color:#666}
.pager{top:2583px;width:24px;height:24px;border:1.5px solid #999;border-radius:50%;display:flex;align-items:center;justify-content:center}

/* testimonials */
.testi-bg{left:0;top:2669px;width:1200px;height:341px;background:linear-gradient(180deg,#1d9fd4 0%,#1588bf 100%)}
.testi-title{color:var(--white)}
.quote{top:2806px;width:300px;color:var(--white);font-size:11.5px;font-style:italic;line-height:1.75}
.quote::before{content:"\201C";font-size:26px;line-height:0;vertical-align:-8px;margin-right:4px}
.author{top:2911px;display:flex;align-items:center;gap:16px}
.avatar{width:72px;height:72px;border-radius:50%;border:3px solid var(--white);background:radial-gradient(circle at 50% 40%,#e3c4a8 0%,#b48866 55%,#7a5c45 100%)}
.author .name{font-family:"Roboto Condensed",sans-serif;font-size:14px;color:var(--white);font-style:italic}
.stars{color:var(--star);font-size:12px;letter-spacing:1px}
.stars i{color:rgba(255,255,255,.6);font-style:normal}

/* footer */
.foot-brand{left:99px;top:3090px;display:flex;align-items:center;gap:12px}
.foot-col h5{font-family:"Roboto Condensed",sans-serif;font-size:17px;font-weight:400;color:#333;margin-bottom:14px}
.foot-col p,.foot-col li{font-size:11.5px;line-height:1.85;color:#555}
.foot-col ul{list-style:none}
.foot-col li{display:flex;align-items:center;gap:8px;line-height:1.95}
.foot-col li::before{content:"";width:9px;height:9px;border-radius:50%;background:#666}
.contact-row{display:flex;align-items:center;gap:12px;margin-top:14px}
.news-input{width:244px;height:40px;border:1px solid var(--line);font-size:11px;color:#777;padding:0 14px;line-height:38px;margin-top:14px}
.news-btn{width:123px;height:32px;margin-top:14px;background:var(--teal);color:var(--white);font-size:11px;font-weight:700;text-align:center;line-height:32px;text-transform:uppercase}
.copy-line{left:0;top:3297px;width:1200px;height:1px;background:#e5e5e5}
.copyright{left:0;top:3324px;width:1200px;text-align:center;font-size:11px;color:#666}
</style>
</head>
<body>

<!-- header -->
<div class="abs brand">
  <span class="brand-dot"></span>
  <span class="brand-name">Bright Kestrel Studio</span>
</div>
<div class="abs head-phone">
  <svg width="20" height="20" viewBox="0 0 24 24"><path fill="#5b2c83" d="M6.6 10.8a15 15 0 0 0 6.6 6.6l2.2-2.2c.3-.3.7-.4 1-.2 1.1.4 2.3.6 3.6.6.6 0 1 .4 1 1V20c0 .6-.4 1-1 1A17 17 0 0 1 3 4c0-.6.4-1 1-1h3.5c.6 0 1 .4 1 1 0 1.3.2 2.5.6 3.6.1.3 0 .7-.2 1z"/></svg>
  (404) 555-0142
</div>
<div class="abs social"><span></span><span></span><span></span><span></span></div>

<nav class="abs nav">
  <ul>
    <li class="active">Home</li><li>About Us</li><li>Courses</li><li>Programs</li><li>Our Team</li><li>Trial Lessons</li><li>Gallery</li><li>Testimonials</li><li>Contact Us</li>
  </ul>
</nav>

<!-- hero -->
<div class="abs hero" role="img" aria-label="Photo of a young girl performing at a recital with a grand piano on stage and an audience seated in front"></div>
<h1 class="abs hero-title">BRIGHT KESTREL STUDIO</h1>
<p class="abs hero-sub">Sed ut perspiciatis unde omnis iste natus sit voluptatem accusantium doloremque</p>
<div class="abs hero-btn">TRIAL LESSONS
  <svg width="12" height="12" viewBox="0 0 12 12"><circle cx="6" cy="6" r="6" fill="#fff"/><path d="M5 3.5 7.5 6 5 8.5" stroke="#ea6330" stroke-width="1.5" fill="none"/></svg>
</div>
<div class="abs hero-arrow" style="left:36px"><svg width="12" height="12" viewBox="0 0 12 12"><path d="M8 1 3 6l5 5" stroke="#fff" stroke-width="2" fill="none"/></svg></div>
<div class="abs hero-arrow" style="left:1132px"><svg width="12" height="12" viewBox="0 0 12 12"><path d="m4 1 5 5-5 5" stroke="#fff" stroke-width="2" fill="none"/></svg></div>

<!-- courses -->
<h2 class="abs sec-title" style="top:716px">OUR COURSES</h2>

<div class="abs course c-yellow" style="left:99px">
  <div class="course-photo" role="img" aria-label="Photo of a student playing drums during a music lesson" style="background:linear-gradient(135deg,#2d2a28,#7b6a5a 60%,#b9a894)"></div>
  <div class="course-body">
    <span class="course-icon"><svg width="20" height="20" viewBox="0 0 20 20"><path d="M8 15V4l8-2v11" stroke="#fff" stroke-width="1.6" fill="none"/><circle cx="6" cy="15" r="2.3" fill="#fff"/><circle cx="14" cy="13" r="2.3" fill="#fff"/></svg></span>
    <h3>MUSIC LESSONS</h3>
    <p>Nemo enim ipsam voluptatem quia voluptas sit aspernatur aut odit aut fugit, sed quia conseq</p>
    <span class="course-btn">READ MORE</span>
  </div>
</div>
<div class="abs course c-blue" style="left:354px">
  <div class="course-photo" role="img" aria-label="Photo of a child painting at an art lesson" style="background:linear-gradient(135deg,#e9e3da,#c9a888 55%,#8d7660)"></div>
  <div class="course-body">
    <span class="course-icon"><svg width="20" height="20" viewBox="0 0 20 20"><circle cx="10" cy="10" r="7" stroke="#fff" stroke-width="1.6" fill="none"/><circle cx="7" cy="8" r="1.3" fill="#fff"/><circle cx="12" cy="7" r="1.3" fill="#fff"/><circle cx="13" cy="12" r="1.3" fill="#fff"/></svg></span>
    <h3>ART LESSONS</h3>
    <p>Nemo enim ipsam voluptatem quia voluptas sit aspernatur aut odit aut fugit, sed quia conseq</p>
    <span class="course-btn">READ MORE</span>
  </div>
</div>
<div class="abs course c-green" style="left:610px">
  <div class="course-photo" role="img" aria-label="Photo of a woman practising yoga outdoors" style="background:linear-gradient(135deg,#e8efe4,#b7c9a4 50%,#7f9a63)"></div>
  <div class="course-body">
    <span class="course-icon"><svg width="20" height="20" viewBox="0 0 20 20"><circle cx="10" cy="4" r="2" fill="#fff"/><path d="M3 9h14M10 7v6l-4 5M10 13l4 5" stroke="#fff" stroke-width="1.6" fill="none"/></svg></span>
    <h3>YOGA CLASSES</h3>
    <p>Nemo enim ipsam voluptatem quia voluptas sit aspernatur aut odit aut fugit, sed quia conseq</p>
    <span class="course-btn">READ MORE</span>
  </div>
</div>
<div class="abs course c-orange" style="left:866px">
  <div class="course-photo" role="img" aria-label="Photo of children acting out a playful scene in a garden" style="background:linear-gradient(135deg,#8fb0c9,#9bb37a 55%,#5e7a3c)"></div>
  <div class="course-body">
    <span class="course-icon"><svg width="20" height="20" viewBox="0 0 20 20"><rect x="3" y="4" width="9" height="10" rx="3" stroke="#fff" stroke-width="1.6" fill="none"/><rect x="8" y="7" width="9" height="10" rx="3" stroke="#fff" stroke-width="1.6" fill="none"/></svg></span>
    <h3>ACTING LESSONS</h3>
    <p>Nemo enim ipsam voluptatem quia voluptas sit aspernatur aut odit aut fugit, sed quia conseq</p>
    <span class="course-btn">READ MORE</span>
  </div>
</div>

<!-- welcome -->
<div class="abs welcome-photo" role="img" aria-label="Photo of a young girl in a black leotard doing a backbend stretch"></div>
<section class="abs welcome">
  <h2>WELCOME TO BRIGHT KESTREL STUDIO</h2>
  <h4>Atlanta's Best Piano, Guitar, Voice, Art Lessons And More, All Taught In Your Home.</h4>
  <p>Learning to play a musical instrument should be an enjoyable journey, not a chore. We exclusively offer in-home, individual music lessons for most instruments including piano, guitar, voice, drums, woodwinds, strings and many more using the unique Bright Kestrel Method. In addition to teaching the fundamentals of reading music we will help you play the styles of music and real songs you are excited to learn!</p>
  <p>Interested in visual arts? Bright Kestrel Studio also offers in-home lessons in drawing, painting and creating small sculptures, either individually or in small groups. You provide the space</p>
  <span class="btn-outline">READ MORE
    <svg width="11" height="11" viewBox="0 0 12 12"><circle cx="6" cy="6" r="6" fill="#666"/><path d="M5 3.5 7.5 6 5 8.5" stroke="#fff" stroke-width="1.5" fill="none"/></svg>
  </span>
</section>

<!-- programs -->
<svg class="abs programs-bg" viewBox="0 0 1200 620" preserveAspectRatio="none">
  <path d="M0 40 Q600 -40 1200 40 L1200 580 Q600 660 0 580 Z" fill="#f1f2f4"/>
  <path d="M0 40 Q600 -40 1200 40" stroke="#e6e7ea" stroke-width="3" fill="none"/>
</svg>
<div class="abs programs-photo" role="img" aria-label="Photo of a young boy in a white shirt and bow tie playing a keyboard"></div>
<section class="abs programs">
  <h2>OUR PROGRAMS</h2>
  <p class="intro">Bright Kestrel Studio offers lessons throughout the entire year via our Weekly and 10-Session Workshop programs. All Bright Kestrel Studio lessons are taught in the comfort and convenience of your own home.</p>
</section>
<div class="abs" style="left:99px;top:1800px;width:560px;height:260px">
  <span class="prog-line" style="top:62px;height:28px"></span>
  <span class="prog-line" style="top:152px;height:28px"></span>
  <div class="prog" style="top:0">
    <span class="prog-icon"><svg width="24" height="24" viewBox="0 0 24 24"><rect x="3" y="5" width="18" height="16" rx="1" stroke="#444" stroke-width="1.6" fill="none"/><path d="M3 9h18M8 3v4M16 3v4M7 13h2M11 13h2M15 13h2M7 17h2M11 17h2" stroke="#444" stroke-width="1.6"/></svg></span>
    <h4>FALL/SPRING PROGRAM</h4>
    <p>This is our primary program, consisting of 36 weekly lessons offered between September and May. Students who would like to begin after the first week</p>
  </div>
  <div class="prog" style="top:90px">
    <span class="prog-icon"><svg width="24" height="24" viewBox="0 0 24 24"><circle cx="12" cy="12" r="9" fill="#444"/><path d="M12 12V3a9 9 0 0 1 9 9z" fill="#fff" stroke="#444" stroke-width="1.2"/></svg></span>
    <h4>10-SESSION WORKSHOPS</h4>
    <p>All workshops in Theater, Music, Visual Arts and Yoga are offered in 10-Session packages which are renewable upon completion. In addition, Music Students who schedule</p>
  </div>
  <div class="prog" style="top:180px">
    <span class="prog-icon"><svg width="26" height="24" viewBox="0 0 26 24"><rect x="5" y="5" width="16" height="11" rx="1" stroke="#444" stroke-width="1.6" fill="none"/><path d="M2 19h22" stroke="#444" stroke-width="2"/></svg></span>
    <h4>TRIAL LESSONS</h4>
    <p>The first two lessons taught are considered "trial" lessons, helping you to determine if our program and the instructor we've offered are exactly right for your needs</p>
  </div>
</div>

<!-- blog -->
<h2 class="abs sec-title" style="top:2189px">LATEST BLOG</h2>
<article class="abs post" style="left:99px">
  <div class="post-photo" role="img" aria-label="Photo of a student band rehearsing together"></div>
  <h3>"All Together Now" April 2013</h3>
  <div class="meta">Jan 21, 2017 <b>\</b> 2 comments</div>
  <p>Lorem ipsum dolor sit amet, consectetur adipiscing<br>Sed blandit massa vel mauris sollicitudin</p>
</article>
<article class="abs post" style="left:444px">
  <div class="post-photo" role="img" aria-label="Photo of a young songwriter singing with a guitar on stage" style="background:linear-gradient(135deg,#1d2a4a,#5b4c6a 50%,#b56a4a)"></div>
  <h3>2014 Student Songwriters'</h3>
  <div class="meta">Jan 21, 2017 <b>\</b> 2 comments</div>
  <p>Lorem ipsum dolor sit amet, consectetur adipiscing<br>Sed blandit massa vel mauris sollicitudin</p>
</article>
<article class="abs post" style="left:792px">
  <div class="post-photo" role="img" aria-label="Photo of students performing drums and keyboard in a studio" style="background:linear-gradient(135deg,#2a1e1a,#8a3e2c 50%,#4a332a)"></div>
  <h3>"All Together Now" April 2012</h3>
  <div class="meta">Jan 21, 2017 <b>\</b> 2 comments</div>
  <p>Lorem ipsum dolor sit amet, consectetur adipiscing<br>Sed blandit massa vel mauris sollicitudin</p>
</article>
<span class="abs pager" style="left:573px"><svg width="8" height="8" viewBox="0 0 8 8"><path d="M5.5 1 2.5 4l3 3" stroke="#777" stroke-width="1.4" fill="none"/></svg></span>
<span class="abs pager" style="left:603px"><svg width="8" height="8" viewBox="0 0 8 8"><path d="m2.5 1 3 3-3 3" stroke="#777" stroke-width="1.4" fill="none"/></svg></span>

<!-- testimonials -->
<div class="abs testi-bg"></div>
<h2 class="abs sec-title testi-title" style="top:2717px">TESTIMONIALS</h2>
<p class="abs quote" style="left:99px">Lorem ipsum dolor sit amet, consectetur adipiscing elit, sed do eiusmod tempor incididunt ut labore et dolore magna aliqua Unde omnis, consequuntur.</p>
<p class="abs quote" style="left:455px">Lorem ipsum dolor sit amet, consectetur adipiscing elit, sed do eiusmod tempor incididunt ut labore et dolore magna aliqua Unde omnis, consequuntur.</p>
<p class="abs quote" style="left:812px">Lorem ipsum dolor sit amet, consectetur adipiscing elit, sed do eiusmod tempor incididunt ut labore et dolore magna aliqua Unde omnis, consequuntur.</p>
<div class="abs author" style="left:99px"><span class="avatar" role="img" aria-label="Portrait photo of the reviewer"></span><div><div class="name">JOHN DOE</div><div class="stars">★★★★<i>★</i></div></div></div>
<div class="abs author" style="left:455px"><span class="avatar" role="img" aria-label="Portrait photo of the reviewer"></span><div><div class="name">JOHN DOE</div><div class="stars">★★★★<i>★</i></div></div></div>
<div class="abs author" style="left:812px"><span class="avatar" role="img" aria-label="Portrait photo of the reviewer"></span><div><div class="name">JOHN DOE</div><div class="stars">★★★★<i>★</i></div></div></div>

<!-- footer -->
<div class="abs foot-brand">
  <span class="brand-dot" style="width:58px;height:58px"></span>
  <span class="brand-name" style="font-size:32px;width:200px">Bright Kestrel Studio</span>
</div>
<div class="abs foot-col" style="left:363px;top:3060px;width:240px">
  <h5>CONTACT US</h5>
  <p>Bright Kestrel Studio, Inc.<br>Larkspur Lane, Maple Hollow and<br>local parks and gardens</p>
  <div class="contact-row"><svg width="18" height="18" viewBox="0 0 24 24"><path fill="none" stroke="#1aa3cc" stroke-width="1.8" d="M6.6 10.8a15 15 0 0 0 6.6 6.6l2.2-2.2c.3-.3.7-.4 1-.2 1.1.4 2.3.6 3.6.6.6 0 1 .4 1 1V20c0 .6-.4 1-1 1A17 17 0 0 1 3 4c0-.6.4-1 1-1h3.5c.6 0 1 .4 1 1 0 1.3.2 2.5.6 3.6.1.3 0 .7-.2 1z"/></svg><p>Phone : (404) 555-0142</p></div>
  <div class="contact-row" style="margin-top:6px"><svg width="18" height="14" viewBox="0 0 20 14"><rect x="1" y="1" width="18" height="12" stroke="#1aa3cc" stroke-width="1.6" fill="none"/><path d="m1 1 9 7 9-7" stroke="#1aa3cc" stroke-width="1.6" fill="none"/></svg><p>Email : info@brightkestrel-studio.test</p></div>
</div>
<div class="abs foot-col" style="left:650px;top:3060px;width:160px">
  <h5>QUICK LINKS</h5>
  <ul><li>Home</li><li>About Us</li><li>Courses</li><li>Programs</li><li>Our Team</li><li>Trial Lessons</li><li>Contact Us</li></ul>
</div>
<div class="abs foot-col" style="left:855px;top:3060px;width:250px">
  <h5>SIGN UP FOR NEWSLETTER</h5>
  <p style="font-size:11px;line-height:1.6">Excepteur sint occaecat cupidatat non proident, sunt in culpa qui officia deserunt</p>
  <div class="news-input">Enter email</div>
  <div class="news-btn">Subscription</div>
</div>
<div class="abs copy-line"></div>
<p class="abs copyright">©2016 - 2017 Bright Kestrel Studio, Inc., All Rights Reserved.</p>

</body>
</html>
```